Design profile for MuroDeck Nordhaven

I had a logo competition here recently, and was left with two logos that I could not choose between. Therefore, I create this competition where I want a complete design package or a visual identity for the company. I want you to create design elements that can be used both in print and online. (letterhead, envelopes, business card, website, facebook, etc.) I have also attached a picture of the car I have ordered. I'm happy if you can show how the design can be used on that as well.
What is important is that the logos are treated individually, and that the design you create reflects or builds up under the logo. I want the design to be recognizable and to have a connection with the logo and what we do. (take fizzo lumo as an example. if you remove the name, but keep the red color and the white line, then you will recognize which brand it is about right away)
You choose whether you want to make proposals only for one logo, or or both, but it is important that they are treated individually. The best overall package determines which logo I use.
I have also added an image that you can use as an example background if you want it in a facebook banner for example.
It is important that the design looks professional and unique. A number of designs have come in, but many of the designs are very similar and general. Here is a video of the printer if you need inspiration: https://clipvault.example/v/Q8ZtrMx2LwK

Industry/Entity Type

WallPrinting

Requirements
Must have
• Unique an professional design that can be used both online and print
Nice to have
• Show how to use the design on a VX Tully. (see photos attached)
Should not have
• The design can be simple, but not too simple and general. I want it to give the company an identity

```html
<!DOCTYPE html>
<html lang="en">
<head>
<meta charset="UTF-8">
<title>MuroDeck Nordhaven – Letterhead</title>
<link rel="stylesheet" href="https://fonts.googleapis.com/css2?family=Lato:wght@400;700&family=Montserrat:wght@400;700&family=Kaushan+Script&display=swap">
<style>
  :root {
    --backdrop: #d9dadb;
    --paper: #ffffff;
    --ink: #2b2b2b;
    --ink-soft: #3a3a3a;
    --brand-blue: #0098d4;
    --brand-orange: #e8661e;
  }
  * { box-sizing: border-box; margin: 0; padding: 0; }
  html, body {
    width: 1200px; height: 960px; overflow: hidden;
    background: var(--backdrop);
  }
  .letterhead {
    position: absolute; left: 282px; top: 30px;
    width: 636px; height: 900px;
    background: var(--paper);
    box-shadow: 0 6px 24px rgba(0,0,0,0.12);
    overflow: hidden;
    font-family: "Lato", sans-serif;
    color: var(--ink);
  }
  .brand {
    position: absolute; left: 52px; top: 92px;
    display: flex; align-items: center; gap: 10px;
  }
  .brand-mark {
    width: 22px; height: 22px; background: var(--ink);
  }
  .brand-name {
    font-family: "Montserrat", sans-serif;
    font-weight: 700; font-size: 21px; letter-spacing: 0.5px;
    color: var(--ink); line-height: 1;
  }
  .contact {
    position: absolute; left: 398px; top: 40px;
    padding-left: 12px;
    border-left: 1.5px solid var(--brand-blue);
    font-family: "Montserrat", sans-serif;
    font-size: 9.5px; line-height: 1.45; color: var(--ink);
  }
  .contact-address { margin-bottom: 5px; }
  .contact-line { display: flex; align-items: center; gap: 5px; }
  .contact-icon { width: 8px; height: 8px; flex: none; }
  .header-rule {
    position: absolute; left: 120px; right: 34px; top: 142px;
    height: 2px; background: var(--brand-blue);
  }
  .letter {
    position: absolute; left: 120px; top: 186px; width: 430px;
    font-size: 11.5px; line-height: 1.4; color: var(--ink-soft);
  }
  .letter-date { margin-bottom: 18px; }
  .recipient { margin-bottom: 14px; }
  .salutation {
    font-weight: 700; font-size: 14px; color: var(--ink);
    margin: 6px 0 12px;
  }
  .letter p.body { margin-bottom: 18px; }
  .closing { margin-top: 6px; }
  .signature {
    font-family: "Kaushan Script", cursive;
    font-size: 30px; color: var(--ink); margin-top: 14px;
  }
  .footer-wave {
    position: absolute; left: 0; top: 0;
    width: 636px; height: 900px;
  }
</style>
</head>
<body>
  <main class="letterhead">
    <svg class="footer-wave" viewBox="0 0 636 900" aria-hidden="true">
      <path d="M398 900 C 470 790, 520 770, 556 680 C 592 590, 600 490, 636 430 L 636 900 Z" fill="var(--brand-blue)"/>
      <path d="M398 900 C 470 790, 520 770, 556 680 C 592 590, 600 490, 636 430" fill="none" stroke="var(--brand-orange)" stroke-width="4"/>
    </svg>

    <header>
      <div class="brand">
        <span class="brand-mark"></span>
        <span class="brand-name">MuroDeck Nordhaven</span>
      </div>

      <address class="contact" style="font-style:normal">
        <div class="contact-address">418 Alder Crest Rd, Unit 7<br>Brookhollow, ON K2P 6R1</div>
        <div class="contact-line">
          <svg class="contact-icon" viewBox="0 0 10 10"><path d="M2 1 L4 1 L4.6 3 L3.4 4 C4 5.4 4.6 6 6 6.6 L7 5.4 L9 6 L9 8 C9 8.6 8.6 9 8 9 C4.2 9 1 5.8 1 2 C1 1.4 1.4 1 2 1 Z" fill="var(--brand-blue)"/></svg>
          011 555 0142
        </div>
        <div class="contact-line">
          <svg class="contact-icon" viewBox="0 0 10 10"><rect x="0.5" y="2" width="9" height="6.5" fill="var(--brand-blue)"/><path d="M0.5 2 L5 5.5 L9.5 2" fill="none" stroke="#fff" stroke-width="0.9"/></svg>
          hello@murodecknordhaven.example
        </div>
        <div class="contact-line">
          <svg class="contact-icon" viewBox="0 0 10 10"><circle cx="5" cy="5" r="4.5" fill="var(--brand-blue)"/><path d="M0.5 5 H9.5 M5 0.5 C3 3, 3 7, 5 9.5 M5 0.5 C7 3, 7 7, 5 9.5" fill="none" stroke="#fff" stroke-width="0.7"/></svg>
          www.murodecknordhaven.example
        </div>
      </address>

      <div class="header-rule"></div>
    </header>

    <section class="letter">
      <div class="letter-date">January-03-2020</div>
      <div class="recipient">Mr, Arvid Lenke<br>President</div>
      <div class="recipient">Brightwell Group<br>123 Street Name, Suite# 10<br>City, State, 120023</div>
      <div class="salutation">Dear Mr, Arvid</div>

      <p class="body">Lorem ipsum dolor sit amet, consectetur adipisicing elit, sed do eiusmod tempor incididunt ut labore et dolore magna aliqua. Ut enim ad minim veniam, quis nostrud exercitation ullamco laboris nisi ut aliquip ex ea commodo consequat. Duis aute irure dolor in reprehenderit in voluptate velit esse cillum dolore eu fugiat nulla pariatur.</p>

      <p class="body">Lorem ipsum dolor sit amet, consectetur adipisicing elit, sed do eiusmod tempor incididunt ut labore et dolore magna aliqua. Ut enim ad minim veniam, quis nostrud exercitation ullamco laboris nisi ut aliquip ex ea commodo consequat. Duis aute irure dolor in reprehenderit in voluptate velit esse cillum dolore eu fugiat nulla pariatur.</p>

      <p class="body">Lorem ipsum dolor sit amet, consectetur adipisicing elit, sed do eiusmod tempor incididunt ut labore et dolore magna aliqua. Ut enim ad minim veniam, quis nostrud exercitation ullamco laboris nisi ut aliquip ex ea commodo consequat.</p>

      <p class="body">Excepteur sint occaecat cupidatat non proident, sunt in culpa qui officia deserunt mollit anim id est laborum. re et dolore magnam aliquam quaerat voluptatem.</p>

      <div class="closing">Regards</div>
      <div class="signature">Henrik Dahl</div>
    </section>
  </main>
</body>
</html>
```